2in1 Bartender & Sommelier needs a business card

I need a business card. I worked as a bartender in many places but I just finished a sommelier school and I would like a new business card. I like minimal design, natural materials and something what makes the people think :) I try to be creative in cocktail making, like little mixology, little twist on recipes... I like to travel and discover new places, cultures and of course interesting drinks and improve continously...live a little bit crazy life. And I like what I do...

Target Market(s)

restaurant/winebar managers, winemakers, other sommeliers and bartenders, people who work in food and beverage sector

Industry/Entity Type

Hospitality

Contact Information for Business Card

Rozsa Tarkany
Bartender & Sommelier
Phone: (FR) +33 6 4827 3190
(HU) +36 70 918 6352

Font styles to use
Script

Requirements
Must have
• Some sign, I am a bartender and sommelier as well.
Nice to have
• black and white maybe with 1 or 2 extra color
Should not have
• very colourful, to many things on the card

```html
<!DOCTYPE html>
<html lang="en">
<head>
<meta charset="utf-8">
<title>Rozsa Tarkany – Bartender &amp; Sommelier</title>
<link rel="stylesheet" href="https://fonts.googleapis.com/css2?family=Great+Vibes&family=Federo&family=Playfair+Display&display=swap">
<style>
  :root {
    --page-bg: #d9d2c8;
    --card-frost: #e6e1dc;
    --card-frost-deep: #cfc8c2;
    --card-black: #000000;
    --card-charcoal: #1e1e1e;
    --wine: #7a1a2a;
    --wine-deep: #5c1424;
    --cherry: #b51f2e;
    --gold: #d8c8a8;
    --gold-soft: #bfae8e;
  }
  * { margin: 0; padding: 0; box-sizing: border-box; }
  html, body {
    width: 1200px;
    height: 970px;
    overflow: hidden;
    background: var(--page-bg);
  }
  .canvas {
    position: relative;
    width: 1200px;
    height: 970px;
  }
  .business-card {
    position: absolute;
    left: 80px;
    top: 189px;
    width: 1040px;
    height: 592px;
    overflow: hidden;
    background: linear-gradient(90deg,
      var(--card-frost) 0%,
      var(--card-frost-deep) 26%,
      var(--card-charcoal) 44%,
      var(--card-black) 62%,
      var(--card-charcoal) 100%);
    box-shadow: 0 10px 30px rgba(0,0,0,0.25);
  }
  .cocktail-art {
    position: absolute;
    left: 0;
    top: 0;
    width: 470px;
    height: 592px;
  }
  .identity {
    position: absolute;
    left: 440px;
    top: 92px;
    width: 560px;
    text-align: center;
  }
  .holder-name {
    font-family: "Great Vibes", cursive;
    font-size: 84px;
    line-height: 1;
    color: var(--wine);
    letter-spacing: 1px;
  }
  .holder-role {
    margin-top: 6px;
    font-family: "Federo", sans-serif;
    font-size: 29px;
    color: var(--gold);
    letter-spacing: 0.5px;
  }
  .contact {
    position: absolute;
    left: 440px;
    top: 400px;
    width: 560px;
    text-align: center;
    font-family: "Playfair Display", serif;
    color: var(--gold);
  }
  .contact-line {
    font-size: 31px;
    line-height: 35px;
  }
  .contact-label {
    color: var(--wine);
  }
  .contact-email {
    margin-top: 14px;
    font-size: 27px;
  }
</style>
</head>
<body>
<div class="canvas">
  <section class="business-card">
    <svg class="cocktail-art" viewBox="0 0 470 592" role="img" aria-label="Illustration of a martini glass with a cherry on a pick and red drink, with small motion strokes">
      <defs>
        <linearGradient id="glassTones" x1="0" y1="0" x2="0" y2="1">
          <stop offset="0" stop-color="var(--cherry)" stop-opacity="0.55"/>
          <stop offset="0.45" stop-color="var(--wine)" stop-opacity="0.75"/>
          <stop offset="1" stop-color="var(--wine-deep)" stop-opacity="0.85"/>
        </linearGradient>
      </defs>
      <rect x="100" y="0" width="360" height="592" fill="url(#glassTones)"/>
    </svg>

    <div class="identity">
      <h1 class="holder-name">Rozsa Tarkany</h1>
      <p class="holder-role">Bartender &amp; Sommelier</p>
    </div>

    <div class="contact">
      <p class="contact-line"><span class="contact-label">(FR)</span> +33 6 4827 3190</p>
      <p class="contact-line"><span class="contact-label">(HU)</span> +36 70 918 6352</p>
      <p class="contact-email"><span class="contact-label">Email:</span> rozsa.tarkany@vinomail.net</p>
    </div>
  </section>
</div>
</body>
</html>
```